Business Card Design Project

I need a business card designed from scratch. I have an existing logo that I can upload in Illustrator for modification or redesign.

The Company is called Rank Harbor http://rankharbor.com.au and we provide Search Engine Optimization services to Australian businesses. The current logo signifies an increase in visitors, profits etc...

There are no restrictions as to the redesign - colours, style etc are all open to change.

Cards will be full colour and one sided printed at http://www.printlorvex.com.au so check their requirements for file format and sizes etc.

I will expect all original files upon completion of project.

Target Market(s)

Any business with a web site looking to improve their search engine rankings

Industry/Entity Type

Business

Requirements
Must have
• I like modern, sleek designs. Clean, not fussy, uncluttered.

```html
<!DOCTYPE html>
<html lang="en">
<head>
<meta charset="utf-8">
<title>Rank Harbor – Business Card</title>
<link rel="stylesheet" href="https://fonts.googleapis.com/css2?family=Mulish:wght@400;700;800&display=swap">
<style>
  :root {
    --page-bg: #e9e7e3;
    --card-white: #ffffff;
    --brand-blue: #1f74b3;
    --brand-blue-dark: #17639c;
    --brand-yellow: #f3d33a;
    --brand-yellow-deep: #e9b92a;
    --text-light: #ffffff;
  }
  * { margin: 0; padding: 0; box-sizing: border-box; }
  html, body {
    width: 1200px;
    height: 900px;
    overflow: hidden;
    background: var(--page-bg);
    font-family: "Mulish", sans-serif;
  }
  .stage {
    width: 1200px;
    height: 900px;
    display: flex;
    align-items: center;
    justify-content: center;
  }
  .business-card {
    width: 840px;
    height: 480px;
    display: flex;
    flex-direction: column;
    box-shadow: 0 18px 40px rgba(0, 0, 0, 0.18);
    overflow: hidden;
  }
  .card-brand {
    flex: 0 0 218px;
    background: var(--card-white);
    display: flex;
    align-items: center;
    justify-content: center;
    gap: 18px;
  }
  .brand-dot {
    width: 34px;
    height: 34px;
    border-radius: 50%;
    background: var(--brand-yellow-deep);
  }
  .brand-name {
    font-size: 62px;
    font-weight: 800;
    color: var(--brand-blue);
    letter-spacing: -0.5px;
  }
  .card-identity {
    flex: 0 0 92px;
    background: linear-gradient(90deg, var(--brand-yellow-deep), var(--brand-yellow) 30%);
    display: flex;
    flex-direction: column;
    align-items: center;
    justify-content: center;
    color: var(--brand-blue-dark);
  }
  .person-name {
    font-size: 34px;
    font-weight: 800;
    letter-spacing: 0.5px;
    line-height: 1.05;
  }
  .person-title {
    font-size: 17px;
    font-weight: 700;
    letter-spacing: 0.8px;
    margin-top: 2px;
  }
  .card-contact {
    flex: 1;
    background: var(--brand-blue);
    color: var(--text-light);
    display: flex;
    flex-direction: column;
    align-items: center;
    justify-content: center;
    gap: 14px;
  }
  .contact-line {
    font-size: 24px;
    font-weight: 400;
  }
  .contact-line .label { font-weight: 800; }
  .contact-web {
    font-size: 27px;
    font-weight: 800;
    letter-spacing: 0.8px;
  }
</style>
</head>
<body>
  <main class="stage">
    <article class="business-card">
      <header class="card-brand">
        <span class="brand-dot" aria-hidden="true"></span>
        <span class="brand-name">Rank Harbor</span>
      </header>
      <section class="card-identity">
        <h1 class="person-name">DALE MERCER</h1>
        <p class="person-title">INTERNET MARKETING CONSULTANT</p>
      </section>
      <section class="card-contact">
        <p class="contact-line"><span class="label">T</span> 1300 482915 · <span class="label">E</span> dale@rankharbor.com.au</p>
        <p class="contact-web">WWW.RANKHARBOR.COM.AU</p>
      </section>
    </article>
  </main>
</body>
</html>
```